Allstar cheerleading team sign ups

We need a flyer to send out to the local schools as well as to put on our website and facebook page.

We are an allstar cheerleading gym that offers competitive cheerleading teams.

We are rolling out a new program called "Half Year Teams". The design is geared towards parents, but should also catch the eye of kids.

Industry/Entity Type

Gym

Requirements
Must have
• Do you want to be an allstar cheerleader? Brindlewood Summit Cheerleading has been one of the top cheerleading training facilities since 2004! Now is your chance to join our family of cheer with less commitment and a fraction of the cost! We are excited to introduce "Half Year Teams"!

The season will run from December to April with each team competing at 3 local competitions. This is a great way to try allstar cheerleading or to cheer during the school offseason!

Team Placement*: Saturday, December 1st at 10:30am
(*Everyone makes a team)

Cost: $115 per month (includes 1 practice per week, choreography/music fees, competition fees)

Uniform: $175 (includes skirt, top, briefs, bow, shoes)

Practice Times: Thursdays 6:45pm-8:30pm

All ages welcome!

www.brindlewood-summit.example
704-219-8853
48216-K Ferncastle Avenue, Charlotte, NC 28941

Must have pictures!

Our colors are carolina blue, black and white- should follow that color scheme.

I am attaching our "Free Classes" flyer to show you an example of what type of design we like.

The logo I am sending is the wrong blue. It should be a light or carolina blue.

```html
<!DOCTYPE html>
<html lang="en">
<head>
<meta charset="utf-8">
<title>Brindlewood Summit Cheerleading – Half Year Teams</title>
<link rel="stylesheet" href="https://fonts.googleapis.com/css2?family=Jost:wght@400;500;600;700;800&display=swap">
<style>
  :root {
    --carolina: #1f8fe0;
    --carolina-deep: #2a6fc4;
    --carolina-light: #5fb6f2;
    --band-light: #8fbdea;
    --ink: #0c1630;
    --black: #111111;
    --white: #ffffff;
    --backdrop: #e9e9e9;
  }
  * { box-sizing: border-box; margin: 0; padding: 0; }
  html, body { width: 1200px; height: 900px; overflow: hidden; }
  body {
    background: var(--backdrop);
    font-family: "Jost", "Futura", sans-serif;
    color: var(--ink);
    position: relative;
  }
  .flyer {
    position: absolute;
    left: 300px; top: 29px;
    width: 600px; height: 842px;
    background: var(--white);
    overflow: hidden;
    box-shadow: 0 2px 10px rgba(0,0,0,.2);
  }
  .flyer-backdrop { position: absolute; inset: 0; }
  .brand-name {
    position: absolute;
    left: 62px; top: 72px; width: 330px;
    text-align: center;
    font-weight: 800;
    font-size: 37px;
    line-height: 66px;
    letter-spacing: 0;
    text-transform: uppercase;
    color: var(--carolina-deep);
  }
  .hero-photo {
    position: absolute;
    left: 402px; top: 140px;
    width: 180px; height: 260px;
    border-radius: 40% 50% 45% 40%;
    background: radial-gradient(ellipse at 55% 55%, #8aa6c2 0%, #c9d4de 45%, rgba(255,255,255,0) 72%);
  }
  .pitch { position: absolute; }
  .pitch-question {
    top: 402px; left: 77px;
    font-weight: 700; font-size: 18px; letter-spacing: .5px;
  }
  .pitch-headline {
    top: 440px; left: 32px;
    font-weight: 700; font-size: 30px; letter-spacing: .5px;
    color: var(--black);
  }
  .pitch-copy {
    text-align: center;
    font-size: 13.5px; line-height: 18px;
  }
  .pitch-copy strong { font-weight: 700; }
  .pitch-intro { top: 494px; left: 34px; width: 492px; }
  .pitch-announce {
    top: 551px; left: 30px; width: 552px; text-align: center;
    font-size: 20px; font-weight: 500; letter-spacing: .2px;
  }
  .pitch-season { top: 584px; left: 46px; width: 482px; }
  .details {
    position: absolute; left: 0; top: 650px;
    width: 600px; height: 98px;
    background: var(--band-light);
    display: grid; grid-template-columns: repeat(4, 1fr);
    padding: 4px 20px 0;
  }
  .detail { text-align: center; font-size: 11px; line-height: 13px; }
  .detail svg { display: block; margin: 0 auto 6px; }
  .detail-title { font-weight: 700; font-size: 11px; text-transform: uppercase; }
  .contact {
    position: absolute; left: 0; top: 748px;
    width: 600px; height: 94px;
    background: var(--carolina-deep);
    text-align: center;
    font-weight: 700; font-size: 14px; line-height: 19px;
    padding-top: 12px;
  }
</style>
</head>
<body>
  <main class="flyer">
    <svg class="flyer-backdrop" width="600" height="842" viewBox="0 0 600 842" aria-hidden="true">
      <defs>
        <linearGradient id="panel-blue" x1="0" y1="0" x2="1" y2="0">
          <stop offset="0" stop-color="#2b6fc6"/>
          <stop offset=".5" stop-color="#1f9be6"/>
          <stop offset="1" stop-color="#2a72c8"/>
        </linearGradient>
        <linearGradient id="fold-shade" x1="0" y1="0" x2="0" y2="1">
          <stop offset="0" stop-color="#ffffff"/>
          <stop offset=".55" stop-color="#cfd6de"/>
          <stop offset="1" stop-color="#1a1a1a"/>
        </linearGradient>
      </defs>
      <path d="M0,222 C90,228 150,276 210,326 S440,448 600,474 L600,842 L0,842 Z" fill="var(--carolina-light)"/>
      <path d="M0,231 C90,237 150,285 210,335 S440,457 600,483 L600,842 L0,842 Z" fill="var(--white)"/>
      <path d="M0,238 C90,244 150,292 210,342 S440,464 600,490 L600,842 L0,842 Z" fill="var(--black)"/>
      <path d="M0,250 C90,256 150,304 210,354 S440,476 600,502 L600,842 L0,842 Z" fill="url(#panel-blue)"/>
      <path d="M176,306 L252,338 L236,380 L160,348 Z" fill="url(#fold-shade)" stroke="var(--black)" stroke-width="2"/>
    </svg>

    <h1 class="brand-name">Brindlewood Summit Cheerleading</h1>

    <div class="hero-photo" role="img" aria-label="Photo of a cheerleader in a blue and black uniform mid-flip"></div>

    <p class="pitch pitch-question">DO YOU WANT TO BE AN</p>
    <h2 class="pitch pitch-headline">ALL STAR CHEERLEADER?</h2>
    <p class="pitch pitch-copy pitch-intro"><strong>Brindlewood Summit Cheerleading</strong> has been one of the top cheerleading training facilities since <strong>2004</strong>! Now is your chance to <strong>join our family</strong> of cheer with less commitment and a <strong>fraction of the cost!</strong></p>
    <p class="pitch pitch-announce">WE ARE EXCITED TO INTRODUCE “HALF YEAR TEAMS”!</p>
    <p class="pitch pitch-copy pitch-season">The season will run from <strong>December to April</strong> with each team competing at <strong>3 local competitions</strong>. This is a <strong>great way to try</strong> allstar cheerleading or to cheer during the <strong>school offseason!</strong></p>

    <section class="details">
      <div class="detail">
        <svg width="30" height="30" viewBox="0 0 30 30" aria-hidden="true"><rect x="3" y="5" width="24" height="22" rx="2" fill="#223"/><rect x="6" y="11" width="18" height="13" fill="#fff"/><rect x="8" y="2" width="3" height="6" fill="#223"/><rect x="19" y="2" width="3" height="6" fill="#223"/><text x="15" y="22" font-size="10" font-weight="700" text-anchor="middle" fill="#223" font-family="Jost, sans-serif">28</text></svg>
        <p class="detail-title">Team Placement</p>
        <p>Saturday December 1st,<br>10:30am<br>(Everyone makes a team)</p>
      </div>
      <div class="detail">
        <svg width="30" height="30" viewBox="0 0 30 30" aria-hidden="true"><text x="15" y="26" font-size="28" font-weight="700" text-anchor="middle" fill="#223" font-family="Jost, sans-serif">$</text></svg>
        <p class="detail-title">$115 per month</p>
        <p>1 Practice per week<br>Choreography &amp; Music Fees<br>Competition Fees</p>
      </div>
      <div class="detail">
        <svg width="30" height="30" viewBox="0 0 30 30" aria-hidden="true"><path d="M4,12 L20,5 L20,25 L4,18 Z" fill="#223"/><rect x="20" y="9" width="5" height="12" fill="#223"/><rect x="7" y="18" width="4" height="8" fill="#223"/></svg>
        <p class="detail-title">Uniform</p>
        <p>$175<br>Includes skirt, top,<br>briefs, bow, shoes</p>
      </div>
      <div class="detail">
        <svg width="30" height="30" viewBox="0 0 30 30" aria-hidden="true"><circle cx="15" cy="16" r="11" fill="none" stroke="#223" stroke-width="3"/><path d="M15,10 L15,16 L19,19" fill="none" stroke="#223" stroke-width="2.5"/><path d="M3,7 L8,2 M27,7 L22,2" stroke="#223" stroke-width="3"/></svg>
        <p class="detail-title">Practice Times</p>
        <p>Thursdays<br>6:45pm-8:30pm</p>
      </div>
    </section>

    <footer class="contact">
      <p>All ages welcome!</p>
      <p>www.brindlewood-summit.example</p>
      <p>704-219-8853</p>
      <p>48216-K Ferncastle Avenue, Charlotte, NC 28941</p>
    </footer>
  </main>
</body>
</html>
```